■依頼の目的/概要
社内活性化目的のポスター制作をお願いしたいです。

■依頼詳細
全社内向けに、部署のミッションを周知するためのポスター制作をお願いいたします。チーム全体のメッセージだけでなく、メンバーそれぞれの熱い思いが伝わる一枚を制作していただきたいです!
※構成は中心に代表者を置き、その周りに添付ファイルのようにメンバー個人写真・目標を入れます。
ポスターのPDFとai(もしくはPSD)データの提出をお願いいたします。

▼レギュレーション
・部署名、部署の半期目標と個人目標・顔写真を入れる
・サイズ:A0もしくはA1
・PDFは塗りたし上下左右3mmを入れる

■重視する点
過去・現在までにデザインの経験のある方を希望致します。

その他何かご不明な点がございましたら、お気軽にご質問下さい。
よろしくお願いいたします。
■依頼の目的/概要
社内活性化目的のポスター制作をお願いしたいです。

■依頼詳細

▼レギュレーション
・部署名、部署の半期目標と個人目標・顔写真を入れる
・サイズ:A0もしくはA1
・PDFは塗りたし上下左右3mmを入れる

■重視する点

よろしくお願いいたします。

遠くから見ても視認性が高く、インパクトのある作品でした。

この度はコンペのご参加ありがとうございました。
機会がございましたらまたお願いいたします。

```html
<!DOCTYPE html>
<html lang="ja">
<head>
<meta charset="UTF-8">
<title>Team Poster</title>
<link rel="stylesheet" href="https://fonts.googleapis.com/css2?family=Montserrat:wght@700;800&family=Noto+Sans+JP:wght@400;700&family=Noto+Serif+JP:wght@500&display=swap">
<style>
:root{
  --green:#8cc21f;
  --green-dark:#6fa40f;
  --green-light:#b5d95c;
  --ink:#222;
  --grey:#555;
  --ring:#d4d4d4;
  --paper:#fff;
}
*{box-sizing:border-box;margin:0;padding:0}
html,body{width:846px;height:1200px;overflow:hidden;background:var(--paper)}
.poster{position:relative;width:846px;height:1200px;font-family:"Noto Sans JP",sans-serif;color:var(--ink)}
.team-name{position:absolute;top:22px;left:0;width:100%;text-align:center;font-family:"Montserrat",sans-serif;font-weight:800;font-size:44px;line-height:56px;color:var(--green);letter-spacing:.5px}
.rule{position:absolute;left:30px;width:786px;height:3px;background:var(--green)}
.rule--top{top:90px}
.rule--bottom{top:960px;height:2px}
.hub-art{position:absolute;left:0;top:0}
.member{position:absolute;width:210px;height:210px;border-radius:50%;background:linear-gradient(#fafafa,#e6e6e6);border:3px solid var(--ring);box-shadow:0 3px 8px rgba(0,0,0,.25);padding:10px}
.member__inner{width:100%;height:100%;border-radius:50%;overflow:hidden;display:flex;flex-direction:column;background:#f4f4f4;border:1px solid #ccc}
.member__photo{flex:0 0 44%;background:linear-gradient(160deg,#d9d3c8,#9e958a)}
.member__goal{flex:0 0 27%;background:var(--green);color:#fff;font-size:10.5px;font-weight:700;line-height:1.5;text-align:center;padding-top:8px}
.member__info{flex:1;text-align:center;padding-top:3px}
.member__role{font-size:7px;color:var(--grey);display:block}
.member__name{font-size:15px;font-weight:700;color:var(--ink);letter-spacing:1px;display:block;line-height:1.3}
.member--top{left:318px;top:163px}
.member--left{left:36px;top:318px}
.member--right{left:600px;top:318px}
.member--lower-left{left:115px;top:586px}
.member--lower-right{left:521px;top:586px}
.leader{left:273px;top:378px;width:300px;height:300px;padding:13px}
.leader .member__goal{font-size:13px;padding-top:6px}
.leader .member__name{font-size:20px}
.leader__label{font-family:"Montserrat",sans-serif;font-size:10px;font-weight:700;display:inline-flex;align-items:center;gap:2px}
.leader__dot{width:11px;height:11px;border-radius:50%;background:var(--ink);display:inline-block}
.season-label{position:absolute;top:838px;width:100%;text-align:center;font-family:"Montserrat",sans-serif;font-weight:700;font-size:15px;color:var(--green-dark)}
.season-title{position:absolute;top:866px;width:100%;text-align:center;font-family:"Noto Serif JP",serif;font-weight:500;font-size:54px;line-height:80px;letter-spacing:6px}
.season-goals{position:absolute;top:990px;left:43px;width:760px;font-size:13px;line-height:2.1;color:var(--green);text-align:center}
</style>
</head>
<body>
<main class="poster">
  <h1 class="team-name">The team's name</h1>
  <div class="rule rule--top"></div>

  <svg class="hub-art" width="846" height="900" viewBox="0 0 846 900" aria-hidden="true">
    <circle cx="423" cy="525" r="300" fill="var(--green)" stroke="var(--green-dark)" stroke-width="3"/>
    <polygon points="423,268 705,423 626,691 220,691 141,423" fill="var(--green-light)" opacity=".65"/>
  </svg>

  <section class="member member--top">
    <div class="member__inner">
      <div class="member__photo" role="img" aria-label="メンバーの顔写真"></div>
      <p class="member__goal">目標スペース、目標スペース、<br>目標スペース、目標スペース、</p>
      <p class="member__info"><span class="member__role">アカウントプランナー</span><span class="member__name">山本 健太</span></p>
    </div>
  </section>
  <section class="member member--left">
    <div class="member__inner">
      <div class="member__photo" role="img" aria-label="メンバーの顔写真"></div>
      <p class="member__goal">目標スペース、目標スペース、<br>目標スペース、目標スペース、</p>
      <p class="member__info"><span class="member__role">プランナー</span><span class="member__name">中村 美咲</span></p>
    </div>
  </section>
  <section class="member member--right">
    <div class="member__inner">
      <div class="member__photo" role="img" aria-label="メンバーの顔写真"></div>
      <p class="member__goal">目標スペース、目標スペース、<br>目標スペース、目標スペース、</p>
      <p class="member__info"><span class="member__role">アカウントプランナー</span><span class="member__name">山本 健太</span></p>
    </div>
  </section>
  <section class="member member--lower-left">
    <div class="member__inner">
      <div class="member__photo" role="img" aria-label="メンバーの顔写真"></div>
      <p class="member__goal">目標スペース、目標スペース、<br>目標スペース、目標スペース、</p>
      <p class="member__info"><span class="member__role">アカウントプランナー</span><span class="member__name">山本 健太</span></p>
    </div>
  </section>
  <section class="member member--lower-right">
    <div class="member__inner">
      <div class="member__photo" role="img" aria-label="メンバーの顔写真"></div>
      <p class="member__goal">目標スペース、目標スペース、<br>目標スペース、目標スペース、</p>
      <p class="member__info"><span class="member__role">プランナー</span><span class="member__name">中村 美咲</span></p>
    </div>
  </section>

  <section class="member leader">
    <div class="member__inner">
      <div class="member__photo" role="img" aria-label="チームリーダーの顔写真"></div>
      <p class="member__goal">目標スペース、目標スペース、<br>目標スペース、目標スペース、<br>目標スペース、目標スペース、</p>
      <p class="member__info">
        <span class="leader__label">Team <i class="leader__dot"></i> Leader</span>
        <span class="member__role">アカウントプランナー</span>
        <span class="member__name">山本 健太</span>
      </p>
    </div>
  </section>

  <p class="season-label">Team's goals for this season</p>
  <h2 class="season-title">今期のチーム目標</h2>
  <div class="rule rule--bottom"></div>
  <p class="season-goals">目標スペース、目標スペース、目標スペース、目標スペース、目標スペース、目標スペース、目標スペース、目標スペース、目標スペース、目標スペース、目標スペース、目標スペース、目標スペース、目標スペース、目標スペース、目標スペース、目標スペース、目標スペース、目標スペース、目標スペース、目標スペース、目標スペース、目標スペース、目標スペース、</p>
</main>
</body>
</html>
```